Bref créative
Business cards and stationary Hospitality group company in Mexico
subtitle is optional "Hospitalidad Hecho en Mexico"
I need double sided standard sized Business Card [3.5" x 2"]
I like the fonts used in my logo but we are open to new fonts or more than one if necessary
Modern
Gerardo Villena
4871 Almendros
Col. Santa Brígida
Monterrey, NL México
CP 67215
beto@qvral.mx
www.qvral.mx
I am looking for a modern design, I like those colors but feel free to play with the colors if you have an idea..
QV ALBERGANTE

```html
<!DOCTYPE html>
<html lang="es">
<head>
<meta charset="utf-8">
<title>QV Albergante — Papelería</title>
<link href="https://fonts.googleapis.com/css2?family=Montserrat:wght@400;600&display=swap" rel="stylesheet">
<style>
:root{
  --stage:#dcdcdc;
  --ink:#2c2a2b;
  --paper:#ffffff;
  --orange:#ee5a2b;
  --red:#e2382a;
  --muted:#8d8b8c;
  --faint:#f1eeec;
}
*{margin:0;padding:0;box-sizing:border-box}
html,body{width:1200px;height:936px;overflow:hidden}
body{background:var(--stage);font-family:'Montserrat',sans-serif;position:relative;color:var(--ink)}
.piece{position:absolute;background:var(--paper);box-shadow:0 2px 6px rgba(0,0,0,.12)}
.brand{display:flex;align-items:center;gap:6px;color:var(--paper);font-weight:600;letter-spacing:.08em;white-space:nowrap}
.brand-dot{background:var(--orange);flex:none}

/* Letterhead */
.letterhead{left:183px;top:68px;width:388px;height:521px}
.letterhead-band{height:58px;background:var(--ink);display:flex;justify-content:space-between;align-items:center;padding:0 14px 0 16px}
.letterhead-band .brand{font-size:10px}
.letterhead-band .brand-dot{width:8px;height:8px}
.contact{list-style:none;font-size:5px;line-height:7.5px;color:#d9d6d5}
.contact li::before{content:"";display:inline-block;width:3px;height:3px;background:var(--red);margin-right:4px;vertical-align:middle}
.letterhead-mark{position:absolute;left:0;right:0;top:240px;text-align:center;color:var(--faint);font-weight:600;font-size:26px;letter-spacing:.08em}

/* Folder */
.folder{left:634px;top:38px;width:462px;height:579px;background:var(--ink)}
.folder .brand{position:absolute;left:0;right:0;top:270px;justify-content:center;font-size:22px}
.folder .brand-dot{width:16px;height:16px}
.folder-band{position:absolute;left:0;right:0;bottom:0;height:26px;background:var(--red);color:var(--paper);font-size:11px;letter-spacing:.12em;text-align:center;line-height:26px}

/* Business cards */
.card{left:46px;width:177px;height:89px;background:var(--ink);display:flex}
.card-front{top:672px}
.card-back{top:779px;align-items:center;justify-content:center}
.card-front .logo-side{width:64px;display:flex;align-items:center;justify-content:center}
.card .brand{font-size:6px}
.card .brand-dot{width:5px;height:5px}
.card-info{flex:1;background:var(--red);color:var(--paper);padding:10px 8px;font-size:5px;line-height:8px}
.card-info .name{font-weight:600;font-size:7px}
.card-back .brand{font-size:10px}
.card-back .brand-dot{width:8px;height:8px}

/* Envelopes */
.envelope-front{left:266px;top:672px;width:432px;height:208px}
.envelope-band{height:54px;background:var(--ink);padding:10px 16px;color:#cfcccb}
.envelope-band .brand{font-size:9px;margin-bottom:8px}
.envelope-band .brand-dot{width:7px;height:7px}
.envelope-band .address{font-size:5px}
.envelope-back{left:738px;top:672px;width:432px;height:208px}
.envelope-back svg{position:absolute;left:0;top:0}
.envelope-back .web{position:absolute;left:0;right:0;top:22px;text-align:center;color:var(--paper);font-size:11px;letter-spacing:.12em}
</style>
</head>
<body>

<section class="piece letterhead">
  <header class="letterhead-band">
    <div class="brand"><span class="brand-dot"></span>QV ALBERGANTE</div>
    <ul class="contact">
      <li>4871 Almendros</li>
      <li>Col. Santa Brígida</li>
      <li>Monterrey, NL México</li>
      <li>CP 67215</li>
      <li>beto@qvral.mx</li>
      <li>T. 81 5550 2190</li>
    </ul>
  </header>
  <div class="letterhead-mark">QV ALBERGANTE</div>
</section>

<section class="piece folder">
  <div class="brand"><span class="brand-dot"></span>QV ALBERGANTE</div>
  <div class="folder-band">www.qvral.mx</div>
</section>

<section class="piece card card-front">
  <div class="logo-side"><div class="brand"><span class="brand-dot"></span>QV ALBERGANTE</div></div>
  <div class="card-info">
    <div class="name">Gerardo Villena</div>
    <div>Director General</div>
    <div>beto@qvral.mx</div>
    <div>www.qvral.mx</div>
  </div>
</section>

<section class="piece card card-back">
  <div class="brand"><span class="brand-dot"></span>QV ALBERGANTE</div>
</section>

<section class="piece envelope-front">
  <div class="envelope-band">
    <div class="brand"><span class="brand-dot"></span>QV ALBERGANTE</div>
    <div class="address">4871 Almendros · Col. Santa Brígida · Monterrey, NL México</div>
  </div>
</section>

<section class="piece envelope-back">
  <svg width="432" height="208" viewBox="0 0 432 208" aria-hidden="true">
    <polygon points="0,0 432,0 432,40 216,84 0,40" fill="var(--orange)"/>
  </svg>
  <div class="web">www.qvral.mx</div>
</section>

</body>
</html>
```